Business Card design for Property Developer

We need a business card design for a Melbourne based Property Developer called "Kestrelmoor Holdings Pty Ltd".

We subdivide land and onsell to builders etc.

We already have a company logo, which is attached. Also I have attached the layout requirements from the printer. We would like a 2-sided design with one side displaying our logo by itself and the other with the required info, such as name, address, tel no., email, abn etc. The card will need to be used by 4 members of staff so name and contact details should be interchangable.
Updates

If possible, can you please write "name' "job position" "phone" "email" "address" on the card but leave them so I can add the details at a later time. Thank you. Also I plan on printing with UV spot printing as a background on the card. Keep this is mind when designing.

Thanks again.

Hello designers, please do not include pics of houses, house plansĀ or construction machinery etc as we really do not like the way it looks. Thank you.

Target Market(s)

Real Estate Agents, Land Owners, Local Council Departments, Govt Bodies, other Developers etc.

Industry/Entity Type

Business

Requirements
Must have
• 2-sided design with one side displaying our logo by itself and the other with the required info, such as name, address, tel no., email, abn etc.

```html
<!DOCTYPE html>
<html lang="en">
<head>
<meta charset="utf-8">
<title>Kestrelmoor Holdings – Business Card</title>
<link href="https://fonts.googleapis.com/css2?family=PT+Sans:ital,wght@0,400;0,700;1,400;1,700&display=swap" rel="stylesheet">
<style>
  :root {
    --backdrop: #9c9d9f;
    --card: #ffffff;
    --accent-blue: #22409a;
    --brand-red: #c8161d;
    --ink: #2b2b2b;
    --ink-soft: #444444;
  }
  html, body {
    margin: 0;
    padding: 0;
    width: 1200px;
    height: 1000px;
    overflow: hidden;
    background: var(--backdrop);
  }
  .canvas {
    position: relative;
    width: 1200px;
    height: 1000px;
    font-family: "PT Sans", sans-serif;
  }
  .card-shapes {
    position: absolute;
    inset: 0;
  }
  .card-body { fill: var(--card); }
  .card-tab { fill: var(--accent-blue); }

  .contact-block {
    position: absolute;
    right: 623px;
    top: 326px;
    text-align: right;
    font-style: italic;
    font-size: 17px;
    line-height: 21px;
    color: var(--ink);
    letter-spacing: 0.3px;
    word-spacing: 2px;
  }
  .contact-block p { margin: 0; }
  .contact-block .line-street { padding-right: 0; }
  .contact-block .line-city { padding-right: 8px; }
  .contact-block .line-tel { padding-right: 10px; }
  .contact-block .line-fax { padding-right: 18px; }
  .contact-block .line-email { padding-right: 33px; }

  .person {
    position: absolute;
    left: 612px;
    top: 355px;
    text-align: center;
    font-style: italic;
    color: var(--ink-soft);
  }
  .person-name {
    margin: 0;
    font-weight: 700;
    font-size: 17px;
    letter-spacing: 0.2px;
  }
  .person-role {
    margin: 0;
    font-size: 14px;
    line-height: 16px;
  }

  .brand-mark {
    position: absolute;
    left: 340px;
    top: 604px;
    width: 180px;
    display: flex;
    flex-direction: column;
    align-items: center;
    gap: 10px;
  }
  .brand-dot {
    width: 58px;
    height: 58px;
    border-radius: 50%;
    background: var(--ink);
  }
  .brand-name {
    margin: 0;
    font-weight: 700;
    font-size: 21px;
    line-height: 22px;
    text-align: center;
    color: var(--brand-red);
  }
</style>
</head>
<body>
<main class="canvas">
  <svg class="card-shapes" width="1200" height="1000" viewBox="0 0 1200 1000" aria-hidden="true">
    <g class="card-front">
      <polygon class="card-body" points="304,293 864,293 805,463 263,463"/>
      <polygon class="card-tab" points="864,293 929,429 813,429"/>
    </g>
    <g class="card-back">
      <polygon class="card-body" points="304,573 864,573 800,744 263,744"/>
      <polygon class="card-tab" points="864,573 929,707 811,707"/>
    </g>
  </svg>

  <section class="contact-block">
    <p class="line-street">218 Larchwood Pde, #412</p>
    <p class="line-city">Hawthorn, VIC 3122</p>
    <p class="line-tel">tel. 5510 3090 / 6610 2281</p>
    <p class="line-fax">fax. 5510 3091 / 6610 2282</p>
    <p class="line-email">rowan@kestrelmoor-holdings.com</p>
  </section>

  <section class="person">
    <p class="person-name">ROWAN ASHDALE</p>
    <p class="person-role">manager</p>
  </section>

  <section class="brand-mark">
    <span class="brand-dot"></span>
    <p class="brand-name">Kestrelmoor Holdings</p>
  </section>
</main>
</body>
</html>
```